Modern Label Design for Fruity Drink (300ml PET)

Dear Graphic Designers,

JOB BRIEF
We are a beverage manufacturer in South Africa seeking a creative wrap-around label design for our exciting new fruity drink range called Zindelu. Although our beverage doesn't contain real fruit, it's crafted to emulate the taste and appearance of authentic fruit juices, complete with essential benefits like vitamins and minerals that are contained in real fruit. Despite being priced competitively, we want the design to exude a premium feel likened to luxury juices and drinks.

TARGET MARKET
The design must possess a modern appeal that resonates with both children and adults.

DESIGN GUIDELINES
- Modern and Elegant
- Colourful
- Evokes a sense of fruit without direct explicit fruit depictions

MANDATORY ELEMENTS
1. Flavoured Drink: Law states that "Flavoured Drink" needs to be written on the front of the label, potentially integrated with the flavor name, e.g., "Orange Flavoured Drink."
2. No Fruit Images: Avoid using real fruit images, opting instead for textures and shapes that very slightly allude to the essence of fruit flavour. This is also a legal constraint.
3. Toucan Mascot: Consider incorporating a toucan or parrot as a potential mascot.
4. Logo: We have a logo, you may use this and adapt it, or design your own.
5. Claims: We need a claim on the front "High in Vitamin C, B and Zinc"

DESIGN INSPIRATION AND WARNING
Avoid drawing inspiration from our initial design attempt, shared in the files section. This design is deemed unsuitable as it appears too busy, has an 'old school' vibe, and may be perceived as exclusively for children. We aspire for a premium design that caters to adults while still being colourful.

FLAVORS
"Golden Swirl" or alternatively "Orange Flavoured Drink"
"Velvet Pop" or alternatively "Berry Flavoured Drink"
"Island Drift" or alternatively "Tropical Flavoured Drink"
"Crisp Meadow" or alternatively "Apple Flavoured Drink"

We encourage your innovative designs. Thank you for your participation, and we look forward to witnessing your creative brilliance!

Best regards,
The Marketing Team

Target Market(s)

Adults and Children (Premium)

Industry/Entity Type

Beverages

Colors

Designer to choose colors to be used in the design.

Requirements
Must have
• Premium and Colourful
Nice to have
• It would be nice to have a new or updated logo (but we have existing logo if needed), and it would be nice to have a parrot or toucan mascot somewhere
Should not have
• Looking too much like a children's fruity drink. Shouldn't contain real images or illustrations of fruit (only vaguely resembling the fruit through shapes and textures)

```html
<!DOCTYPE html>
<html lang="en">
<head>
<meta charset="utf-8">
<title>Zindelu – Flavoured Drink Label Range</title>
<link rel="stylesheet" href="https://fonts.googleapis.com/css2?family=Bebas+Neue&family=Roboto+Condensed:wght@400;700&display=swap">
<style>
:root{
  --page:#ffffff;
  --white:#ffffff;
  --orange-bg:#f15a2b; --orange-badge:#f7941d; --orange-accent:#e8501f; --orange-claim:#f7941d;
  --berry-bg:#572c7f; --berry-badge:#e4197b; --berry-accent:#6a2c8c; --berry-claim:#e4197b;
  --teal-bg:#10807f; --teal-badge:#4fc3b7; --teal-accent:#0f7a78; --teal-claim:#4fc3b7;
  --green-bg:#0f9447; --green-badge:#4bb848; --green-accent:#138a3f; --green-claim:#a8cf38;
  --fruit-orange:#f7941d; --fruit-berry:#e4197b; --fruit-teal:#f4e61b; --fruit-green:#a8cf38;
  --mascot-orange:#4fc3b7; --mascot-berry:#6a2c8c; --mascot-teal:#0f7a78; --mascot-green:#e8332a;
}
*{margin:0;padding:0;box-sizing:border-box}
html,body{width:1200px;height:780px;overflow:hidden;background:var(--page)}
.canvas{position:relative;width:1200px;height:780px}
.label{position:absolute;left:273px;width:653px;height:131px;background:var(--bg);overflow:hidden;color:var(--white);font-family:"Roboto Condensed",sans-serif}
.label--orange{top:90px;--bg:var(--orange-bg);--badge:var(--orange-badge);--accent:var(--orange-accent);--claim:var(--orange-claim);--fruit:var(--fruit-orange);--mascot:var(--mascot-orange)}
.label--berry{top:242px;--bg:var(--berry-bg);--badge:var(--berry-badge);--accent:var(--berry-accent);--claim:var(--berry-claim);--fruit:var(--fruit-berry);--mascot:var(--mascot-berry)}
.label--teal{top:393px;--bg:var(--teal-bg);--badge:var(--teal-badge);--accent:var(--teal-accent);--claim:var(--teal-claim);--fruit:var(--fruit-teal);--mascot:var(--mascot-teal)}
.label--green{top:544px;--bg:var(--green-bg);--badge:var(--green-badge);--accent:var(--green-accent);--claim:var(--green-claim);--fruit:var(--fruit-green);--mascot:var(--mascot-green)}
.glue-tab{position:absolute;left:0;top:62px;width:15px;height:60px;background:var(--page)}
.date-panel{position:absolute;left:591px;top:62px;width:59px;height:60px;background:var(--white)}
.producer{position:absolute;left:127px;top:34px;width:70px;font-size:4.3px;line-height:4.6px}
.careline{position:absolute;left:127px;top:84px;font-size:4.3px;line-height:4.6px}
.storage{position:absolute;left:127px;top:92px;font-family:"Bebas Neue",sans-serif;font-size:7.2px;line-height:9px}
.volume{position:absolute;left:209px;top:94px;font-family:"Bebas Neue",sans-serif;font-size:11px;letter-spacing:.3px}
.badge{position:absolute;left:262px;top:1px;width:130px;height:130px}
.badge-disc{position:absolute;inset:0;border-radius:50%;background:var(--badge)}
.mascot{position:absolute;left:96px;top:50px;width:30px;height:58px}
.brand{position:absolute;left:0;width:110px;top:22px;text-align:center;font-family:"Bebas Neue",sans-serif;font-size:34px;line-height:34px;color:var(--white);letter-spacing:1px}
.flavour{position:absolute;left:0;width:130px;top:81px;text-align:center;font-family:"Bebas Neue",sans-serif;font-size:16px;line-height:16px;color:var(--white);letter-spacing:.6px}
.legal-name{position:absolute;left:0;width:120px;top:95px;text-align:center;font-family:"Bebas Neue",sans-serif;font-size:13px;line-height:13px;color:var(--accent);letter-spacing:.3px}
.fruit-cue{position:absolute;left:400px;top:9px;width:42px;height:42px}
.claim{position:absolute;left:420px;width:60px;top:70px;text-align:center;font-family:"Bebas Neue",sans-serif;font-size:11px;line-height:12px;color:var(--claim);letter-spacing:.3px}
.claim b{color:var(--white);font-weight:400}
.ingredients{position:absolute;left:476px;top:9px;width:110px;font-size:3.4px;line-height:4.1px}
.nutrition{position:absolute;left:490px;top:39px;width:90px;font-size:3.4px;line-height:5.2px;border-collapse:collapse}
.nutrition caption{text-align:left;font-weight:700}
.nutrition td,.nutrition th{padding:0;font-weight:400;text-align:center}
.nutrition td:first-child{text-align:left;width:48px}
.nutrition-note{position:absolute;left:490px;top:114px;width:95px;font-size:3.4px;line-height:4.2px}
.origin{position:absolute;left:584px;top:120px;transform-origin:left top;transform:rotate(-90deg);font-size:4px;font-weight:700;white-space:nowrap}
</style>
</head>
<body>
<main class="canvas">

<section class="label label--orange" aria-label="Golden Swirl label">
  <div class="glue-tab"></div>
  <p class="producer">Bottled at Source. Specially packed by RIVERBEND BOTTLING COMPANY (Pty) Ltd, Plot 41, Kliprand West, Gauteng, South Africa.</p>
  <p class="careline">Careline 0861 555 018<br>www.riverbendwater.co.za</p>
  <p class="storage">STORE IN<br>A COOL<br>DRY PLACE</p>
  <p class="volume">300ML</p>
  <div class="badge">
    <div class="badge-disc"></div>
    <svg class="mascot" viewBox="0 0 30 58" role="img" aria-label="Toucan mascot illustration"><rect x="0" y="0" width="30" height="58" rx="14" fill="var(--mascot)"/></svg>
    <p class="brand">Zindelu</p>
    <p class="flavour">GOLDEN SWIRL</p>
    <p class="legal-name">FLAVOURED DRINK</p>
  </div>
  <svg class="fruit-cue" viewBox="0 0 42 42" role="img" aria-label="Citrus texture motif"><circle cx="21" cy="21" r="21" fill="var(--fruit)"/></svg>
  <p class="claim">HIGH IN<br>VITAMIN<br><b>C, B, ZN</b></p>
  <p class="ingredients"><b>INGREDIENTS</b> Mineral Water, Sugar, Citric Acid (E330), Flavourings, Stabiliser (E415), Sodium Cyclamate, Acesulfame K, Aspartame* (non-nutritive sweeteners), Preservative (Sodium Benzoate E211), Colourants, Malic Acid (E296), Vitamins (Vitamin C, Vitamin B6), Zinc Sulphate. *Contains Phenylalanine.</p>
  <table class="nutrition">
    <caption>TYPICAL NUTRITIONAL INFORMATION</caption>
    <tr><td></td><th>Per 100ml</th><th>Per 300ml</th><th>%NRV</th></tr>
    <tr><td>Energy (kJ)</td><td>62</td><td>186</td><td></td></tr>
    <tr><td>Protein (g)</td><td>0</td><td>0</td><td></td></tr>
    <tr><td>Glycaemic Carbohydrate (g)</td><td>4</td><td>12</td><td></td></tr>
    <tr><td>of which total sugar (g)</td><td>4</td><td>12</td><td></td></tr>
    <tr><td>Total Fat (g)</td><td>0</td><td>0</td><td></td></tr>
    <tr><td>of which Saturated fat (g)</td><td>0</td><td>0</td><td></td></tr>
    <tr><td>Dietary Fibre, Total (g)</td><td>0</td><td>0</td><td></td></tr>
    <tr><td>Total Sodium (mg)</td><td>13</td><td>39</td><td></td></tr>
    <tr><td>Vitamin C (mg)</td><td>10</td><td>30</td><td>30</td></tr>
    <tr><td>Vitamin B6 (mcg)</td><td>40</td><td>120</td><td>30</td></tr>
    <tr><td>Zinc (mg)</td><td>1</td><td>3</td><td>30</td></tr>
  </table>
  <p class="nutrition-note">*NRV = Nutrient reference value for individuals 4 years &amp; older per serving. Theoretically calculated.</p>
  <p class="origin">Produced in South Africa</p>
  <div class="date-panel"></div>
</section>

<section class="label label--berry" aria-label="Velvet Pop label">
  <div class="glue-tab"></div>
  <p class="producer">Bottled at Source. Specially packed by RIVERBEND BOTTLING COMPANY (Pty) Ltd, Plot 41, Kliprand West, Gauteng, South Africa.</p>
  <p class="careline">Careline 0861 555 018<br>www.riverbendwater.co.za</p>
  <p class="storage">STORE IN<br>A COOL<br>DRY PLACE</p>
  <p class="volume">300ML</p>
  <div class="badge">
    <div class="badge-disc"></div>
    <svg class="mascot" viewBox="0 0 30 58" role="img" aria-label="Toucan mascot illustration"><rect x="0" y="0" width="30" height="58" rx="14" fill="var(--mascot)"/></svg>
    <p class="brand">Zindelu</p>
    <p class="flavour">VELVET POP</p>
    <p class="legal-name">FLAVOURED DRINK</p>
  </div>
  <svg class="fruit-cue" viewBox="0 0 42 42" role="img" aria-label="Berry cluster motif"><circle cx="21" cy="21" r="21" fill="var(--fruit)"/></svg>
  <p class="claim">HIGH IN<br>VITAMIN<br><b>C, B, ZN</b></p>
  <p class="ingredients"><b>INGREDIENTS</b> Mineral Water, Sugar, Citric Acid (E330), Flavourings, Stabiliser (E415), Sodium Cyclamate, Acesulfame K, Aspartame* (non-nutritive sweeteners), Preservative (Sodium Benzoate E211), Colourants, Malic Acid (E296), Vitamins (Vitamin C, Vitamin B6), Zinc Sulphate. *Contains Phenylalanine.</p>
  <table class="nutrition">
    <caption>TYPICAL NUTRITIONAL INFORMATION</caption>
    <tr><td></td><th>Per 100ml</th><th>Per 300ml</th><th>%NRV</th></tr>
    <tr><td>Energy (kJ)</td><td>62</td><td>186</td><td></td></tr>
    <tr><td>Protein (g)</td><td>0</td><td>0</td><td></td></tr>
    <tr><td>Glycaemic Carbohydrate (g)</td><td>4</td><td>12</td><td></td></tr>
    <tr><td>of which total sugar (g)</td><td>4</td><td>12</td><td></td></tr>
    <tr><td>Total Fat (g)</td><td>0</td><td>0</td><td></td></tr>
    <tr><td>of which Saturated fat (g)</td><td>0</td><td>0</td><td></td></tr>
    <tr><td>Dietary Fibre, Total (g)</td><td>0</td><td>0</td><td></td></tr>
    <tr><td>Total Sodium (mg)</td><td>13</td><td>39</td><td></td></tr>
    <tr><td>Vitamin C (mg)</td><td>10</td><td>30</td><td>30</td></tr>
    <tr><td>Vitamin B6 (mcg)</td><td>40</td><td>120</td><td>30</td></tr>
    <tr><td>Zinc (mg)</td><td>1</td><td>3</td><td>30</td></tr>
  </table>
  <p class="nutrition-note">*NRV = Nutrient reference value for individuals 4 years &amp; older per serving. Theoretically calculated.</p>
  <p class="origin">Produced in South Africa</p>
  <div class="date-panel"></div>
</section>

<section class="label label--teal" aria-label="Island Drift label">
  <div class="glue-tab"></div>
  <p class="producer">Bottled at Source. Specially packed by RIVERBEND BOTTLING COMPANY (Pty) Ltd, Plot 41, Kliprand West, Gauteng, South Africa.</p>
  <p class="careline">Careline 0861 555 018<br>www.riverbendwater.co.za</p>
  <p class="storage">STORE IN<br>A COOL<br>DRY PLACE</p>
  <p class="volume">300ML</p>
  <div class="badge">
    <div class="badge-disc"></div>
    <svg class="mascot" viewBox="0 0 30 58" role="img" aria-label="Toucan mascot illustration"><rect x="0" y="0" width="30" height="58" rx="14" fill="var(--mascot)"/></svg>
    <p class="brand">Zindelu</p>
    <p class="flavour">ISLAND DRIFT</p>
    <p class="legal-name">FLAVOURED DRINK</p>
  </div>
  <svg class="fruit-cue" viewBox="0 0 42 42" role="img" aria-label="Tropical ring motif"><circle cx="21" cy="21" r="21" fill="var(--fruit)"/></svg>
  <p class="claim">HIGH IN<br>VITAMIN<br><b>C, B, ZN</b></p>
  <p class="ingredients"><b>INGREDIENTS</b> Mineral Water, Sugar, Citric Acid (E330), Flavourings, Stabiliser (E415), Sodium Cyclamate, Acesulfame K, Aspartame* (non-nutritive sweeteners), Preservative (Sodium Benzoate E211), Colourants, Malic Acid (E296), Vitamins (Vitamin C, Vitamin B6), Zinc Sulphate. *Contains Phenylalanine.</p>
  <table class="nutrition">
    <caption>TYPICAL NUTRITIONAL INFORMATION</caption>
    <tr><td></td><th>Per 100ml</th><th>Per 300ml</th><th>%NRV</th></tr>
    <tr><td>Energy (kJ)</td><td>62</td><td>186</td><td></td></tr>
    <tr><td>Protein (g)</td><td>0</td><td>0</td><td></td></tr>
    <tr><td>Glycaemic Carbohydrate (g)</td><td>4</td><td>12</td><td></td></tr>
    <tr><td>of which total sugar (g)</td><td>4</td><td>12</td><td></td></tr>
    <tr><td>Total Fat (g)</td><td>0</td><td>0</td><td></td></tr>
    <tr><td>of which Saturated fat (g)</td><td>0</td><td>0</td><td></td></tr>
    <tr><td>Dietary Fibre, Total (g)</td><td>0</td><td>0</td><td></td></tr>
    <tr><td>Total Sodium (mg)</td><td>13</td><td>39</td><td></td></tr>
    <tr><td>Vitamin C (mg)</td><td>10</td><td>30</td><td>30</td></tr>
    <tr><td>Vitamin B6 (mcg)</td><td>40</td><td>120</td><td>30</td></tr>
    <tr><td>Zinc (mg)</td><td>1</td><td>3</td><td>30</td></tr>
  </table>
  <p class="nutrition-note">*NRV = Nutrient reference value for individuals 4 years &amp; older per serving. Theoretically calculated.</p>
  <p class="origin">Produced in South Africa</p>
  <div class="date-panel"></div>
</section>

<section class="label label--green" aria-label="Crisp Meadow label">
  <div class="glue-tab"></div>
  <p class="producer">Bottled at Source. Specially packed by RIVERBEND BOTTLING COMPANY (Pty) Ltd, Plot 41, Kliprand West, Gauteng, South Africa.</p>
  <p class="careline">Careline 0861 555 018<br>www.riverbendwater.co.za</p>
  <p class="storage">STORE IN<br>A COOL<br>DRY PLACE</p>
  <p class="volume">300ML</p>
  <div class="badge">
    <div class="badge-disc"></div>
    <svg class="mascot" viewBox="0 0 30 58" role="img" aria-label="Toucan mascot illustration"><rect x="0" y="0" width="30" height="58" rx="14" fill="var(--mascot)"/></svg>
    <p class="brand">Zindelu</p>
    <p class="flavour">CRISP MEADOW</p>
    <p class="legal-name">FLAVOURED DRINK</p>
  </div>
  <svg class="fruit-cue" viewBox="0 0 42 42" role="img" aria-label="Apple shape motif"><circle cx="21" cy="21" r="21" fill="var(--fruit)"/></svg>
  <p class="claim">HIGH IN<br>VITAMIN<br><b>C, B, ZN</b></p>
  <p class="ingredients"><b>INGREDIENTS</b> Mineral Water, Sugar, Citric Acid (E330), Flavourings, Stabiliser (E415), Sodium Cyclamate, Acesulfame K, Aspartame* (non-nutritive sweeteners), Preservative (Sodium Benzoate E211), Colourants, Malic Acid (E296), Vitamins (Vitamin C, Vitamin B6), Zinc Sulphate. *Contains Phenylalanine.</p>
  <table class="nutrition">
    <caption>TYPICAL NUTRITIONAL INFORMATION</caption>
    <tr><td></td><th>Per 100ml</th><th>Per 300ml</th><th>%NRV</th></tr>
    <tr><td>Energy (kJ)</td><td>62</td><td>186</td><td></td></tr>
    <tr><td>Protein (g)</td><td>0</td><td>0</td><td></td></tr>
    <tr><td>Glycaemic Carbohydrate (g)</td><td>4</td><td>12</td><td></td></tr>
    <tr><td>of which total sugar (g)</td><td>4</td><td>12</td><td></td></tr>
    <tr><td>Total Fat (g)</td><td>0</td><td>0</td><td></td></tr>
    <tr><td>of which Saturated fat (g)</td><td>0</td><td>0</td><td></td></tr>
    <tr><td>Dietary Fibre, Total (g)</td><td>0</td><td>0</td><td></td></tr>
    <tr><td>Total Sodium (mg)</td><td>13</td><td>39</td><td></td></tr>
    <tr><td>Vitamin C (mg)</td><td>10</td><td>30</td><td>30</td></tr>
    <tr><td>Vitamin B6 (mcg)</td><td>40</td><td>120</td><td>30</td></tr>
    <tr><td>Zinc (mg)</td><td>1</td><td>3</td><td>30</td></tr>
  </table>
  <p class="nutrition-note">*NRV = Nutrient reference value for individuals 4 years &amp; older per serving. Theoretically calculated.</p>
  <p class="origin">Produced in South Africa</p>
  <div class="date-panel"></div>
</section>

</main>
</body>
</html>
```